Manuka honey wholesales and exports

We need business cards for our honey distribution company based in New Zealand. We supply shops locally and export Manuka honey around the world.
We deal with a very high quality and 100% natural product that can be used for medical, general health as well as food. We are looking business cards that show our honey products are of a high quality with a modern look.

Target Market(s)

Health and medical retailers and importers

Industry/Entity Type

Wholesale

Contact Information for Business Card

Tevin Apiary NZ Limited

www.tevinapiarynz.example

Derek Fawley

M +64 219036482

E tevinapiarynz@mailbox.example

PO Box 58-214
Takapuna
North Shore
Auckland
New Zealand

Font styles to use
Serif

Requirements
Must have
• (Tevin Apiary NZ Limited) with some artwork on one side and all details on the other side.
Nice to have
• I have seen a very simple card with large yellow and black stripes on one side with a company name.. looked clean and simple so something similar or just let the creative beast inside you take over and we will see what you can come up with.

```html
<!DOCTYPE html>
<html lang="en">
<head>
<meta charset="utf-8">
<title>Tevin Apiary NZ Limited — Business Card</title>
<link rel="stylesheet" href="https://fonts.googleapis.com/css2?family=Quicksand:wght@400;500&family=Roboto:wght@300;400;700&display=swap">
<style>
  :root {
    --backdrop: #3a3a3c;
    --card-top: #2a2a2c;
    --card-bottom: #1c1c1e;
    --honey: #f0dd1c;
    --honey-deep: #d9c410;
    --ink-light: #f2f2f2;
    --ink-muted: #c9c9c9;
  }
  * { box-sizing: border-box; margin: 0; padding: 0; }
  html, body { width: 1200px; height: 1000px; overflow: hidden; }
  body {
    background: var(--backdrop);
    position: relative;
    font-family: "Roboto", Arial, sans-serif;
  }
  .card {
    position: absolute;
    top: 180px;
    width: 380px;
    height: 640px;
    background: linear-gradient(160deg, var(--card-top), var(--card-bottom));
    box-shadow: 0 18px 40px rgba(0,0,0,.45);
    color: var(--ink-light);
    overflow: hidden;
  }
  .card--details { left: 170px; }
  .card--name { left: 650px; }
  .card__bands { position: absolute; inset: 0; }
  .brand {
    position: absolute;
    left: 0; right: 0;
    display: flex;
    flex-direction: column;
    align-items: center;
    text-align: center;
  }
  .brand__mark {
    width: 46px; height: 46px;
    border-radius: 50%;
    background: var(--honey);
    margin-bottom: 16px;
  }
  .brand__name {
    font-family: "Quicksand", Arial, sans-serif;
    font-weight: 500;
    font-size: 25px;
    color: var(--honey);
    letter-spacing: .2px;
  }
  .brand__web {
    font-family: "Quicksand", Arial, sans-serif;
    font-size: 12.5px;
    letter-spacing: 2.6px;
    color: var(--ink-muted);
    margin-top: 8px;
  }
  .card--details .brand { top: 120px; }
  .card--name .brand { top: 140px; }
  .ribbon {
    position: absolute;
    top: 290px; left: 40px;
    width: 300px; height: 44px;
  }
  .ribbon__text {
    position: absolute;
    inset: 0;
    display: flex; align-items: center; justify-content: center;
    font-family: "Quicksand", Arial, sans-serif;
    font-size: 15px;
    color: #2a2a2c;
    letter-spacing: .4px;
  }
  .address {
    position: absolute;
    top: 370px; left: 0; right: 0;
    text-align: center;
    font-weight: 300;
    font-size: 15px;
    line-height: 1.45;
    color: var(--ink-muted);
  }
  .address__pin { display: block; margin: 0 auto 10px; }
  .contacts {
    position: absolute;
    top: 480px; left: 50px;
    list-style: none;
  }
  .contacts__item {
    display: flex; align-items: center; gap: 12px;
    font-weight: 300;
    font-size: 15px;
    color: var(--ink-muted);
    margin-bottom: 12px;
  }
  .icon-dot {
    width: 24px; height: 24px;
    border-radius: 50%;
    background: var(--honey);
    display: flex; align-items: center; justify-content: center;
    flex-shrink: 0;
  }
  .person {
    position: absolute;
    top: 380px; left: 0; right: 0;
    text-align: center;
    font-weight: 700;
    font-size: 34px;
    letter-spacing: .5px;
  }
  .person__first { color: var(--ink-light); }
  .person__last { color: var(--honey); }
</style>
</head>
<body>

<section class="card card--details" aria-label="Card back with contact details">
  <svg class="card__bands" width="380" height="640" viewBox="0 0 380 640" aria-hidden="true">
    <polygon points="20,0 330,0 310,24 0,24" fill="var(--honey)"/>
    <polygon points="150,640 370,640 380,616 170,616" fill="var(--honey)"/>
  </svg>

  <div class="brand">
    <span class="brand__mark" aria-hidden="true"></span>
    <span class="brand__name">Tevin Apiary NZ Limited</span>
  </div>

  <div class="ribbon">
    <svg width="300" height="44" viewBox="0 0 300 44" aria-hidden="true">
      <polygon points="0,44 12,8 300,0 288,36" fill="var(--honey)"/>
      <polygon points="288,36 300,0 300,8" fill="var(--honey-deep)"/>
    </svg>
    <span class="ribbon__text">www.tevinapiarynz.example</span>
  </div>

  <address class="address" style="font-style:normal">
    <svg class="address__pin" width="24" height="24" viewBox="0 0 24 24" aria-hidden="true">
      <circle cx="12" cy="12" r="12" fill="var(--honey)"/>
      <path d="M12 5.5a4 4 0 0 0-4 4c0 3 4 8 4 8s4-5 4-8a4 4 0 0 0-4-4z" fill="none" stroke="#2a2a2c" stroke-width="1.4"/>
      <circle cx="12" cy="9.5" r="1.4" fill="#2a2a2c"/>
    </svg>
    PO Box 58-214 Takapuna North Shore,<br>Auckland New Zealand
  </address>

  <ul class="contacts">
    <li class="contacts__item">
      <span class="icon-dot" aria-hidden="true">
        <svg width="14" height="14" viewBox="0 0 24 24"><path d="M6.6 10.8a15 15 0 0 0 6.6 6.6l2.2-2.2a1 1 0 0 1 1-.25 11.4 11.4 0 0 0 3.6.6 1 1 0 0 1 1 1V20a1 1 0 0 1-1 1A17 17 0 0 1 3 4a1 1 0 0 1 1-1h3.5a1 1 0 0 1 1 1c0 1.25.2 2.45.6 3.6a1 1 0 0 1-.25 1z" fill="#2a2a2c"/></svg>
      </span>
      +64 219 036 482
    </li>
    <li class="contacts__item">
      <span class="icon-dot" aria-hidden="true">
        <svg width="14" height="14" viewBox="0 0 24 24"><rect x="3" y="6" width="18" height="12" fill="none" stroke="#2a2a2c" stroke-width="2"/><path d="M3 6l9 7 9-7" fill="none" stroke="#2a2a2c" stroke-width="2"/></svg>
      </span>
      tevinapiarynz@mailbox.example
    </li>
  </ul>
</section>

<section class="card card--name" aria-label="Card front with name">
  <svg class="card__bands" width="380" height="640" viewBox="0 0 380 640" aria-hidden="true">
    <polygon points="50,0 290,0 270,24 30,24" fill="var(--honey)"/>
    <polygon points="160,640 370,640 380,616 180,616" fill="var(--honey)"/>
  </svg>

  <div class="brand">
    <span class="brand__mark" aria-hidden="true"></span>
    <span class="brand__name">Tevin Apiary NZ Limited</span>
    <span class="brand__web">www.tevinapiarynz.example</span>
  </div>

  <h1 class="person">
    <span class="person__first">DEREK</span>
    <span class="person__last">FAWLEY</span>
  </h1>
</section>

</body>
</html>
```